Lanterns After Rain - CD cover indie music

This is my 4th and final album. I am sharing my story of trials, pain and persistence that led me here, like a sound track to a short film.
I would like a design that communicates both a painful phase of life, yet tranquility and beauty found as life winds down. Can be illustrated or photograph.
On front design should have title 'Lanterns After Rain' and artist name.
I will need to add credits and song list.
I am thinking a booklet will be added with lyrics and a few photos and plan to work with this artist. Thank you

Target Market(s)

Folk, easy listening, story telling

Industry/Entity Type

Indie music - independent

Font styles to use
Sans Serif
Other font styles liked:
• I like also verdana font.

Requirements
Nice to have
• a contrast of colors to emotions may work well. There is a portuguese word ‘saudade’ that expresses sadness, but longing also.
Should not have
• No bright red. Not busy. No images of people or animals.

```html
<!DOCTYPE html>
<html lang="en">
<head>
<meta charset="utf-8">
<title>Lanterns After Rain — Evan Hollis</title>
<link href="https://fonts.googleapis.com/css2?family=Playfair+Display:wght@600;700&display=swap" rel="stylesheet">
<style>
  :root {
    --paper: #f5ecdc;
    --ink-orange: #d27b3b;
    --sun-light: #eba062;
    --sun-deep: #db7838;
    --rock-dark: #4f4e4b;
    --rock-light: #b8b3aa;
    --sand: #e8b783;
    --rust: #cf6a30;
  }
  html, body {
    margin: 0;
    padding: 0;
    width: 1200px;
    height: 1200px;
    overflow: hidden;
    background: var(--paper);
  }
  .cover {
    position: relative;
    width: 1200px;
    height: 1200px;
    background: var(--paper);
    font-family: "Playfair Display", Georgia, serif;
  }
  .cover-art {
    position: absolute;
    inset: 0;
    width: 1200px;
    height: 1200px;
  }
  .numeral {
    font-family: "Playfair Display", Georgia, serif;
    font-weight: 700;
    fill: var(--paper);
  }
  .artist {
    position: absolute;
    left: 63px;
    top: 888px;
    margin: 0;
    font-size: 42px;
    font-weight: 600;
    line-height: 1;
    letter-spacing: 0.08em;
    color: var(--ink-orange);
  }
  .title {
    position: absolute;
    left: 60px;
    top: 930px;
    margin: 0;
    color: var(--ink-orange);
    font-weight: 700;
    line-height: 1;
  }
  .title-line {
    display: flex;
    align-items: center;
    font-size: 106px;
    height: 108px;
  }
  .title-connector {
    display: inline-block;
    margin-left: 26px;
    padding: 10px 4px 8px;
    font-size: 28px;
    font-weight: 600;
    letter-spacing: 0.06em;
    border-top: 2px solid var(--ink-orange);
    border-bottom: 2px solid var(--ink-orange);
    line-height: 1;
    position: relative;
    top: 8px;
  }
</style>
</head>
<body>
<main class="cover">
  <svg class="cover-art" viewBox="0 0 1200 1200" xmlns="http://www.w3.org/2000/svg">
    <defs>
      <linearGradient id="sunFill" x1="0" y1="0" x2="0" y2="1">
        <stop offset="0" stop-color="var(--sun-light)"/>
        <stop offset="1" stop-color="var(--sun-deep)"/>
      </linearGradient>
      <linearGradient id="landFill" x1="0" y1="0" x2="0" y2="1">
        <stop offset="0" stop-color="var(--rock-dark)"/>
        <stop offset="0.35" stop-color="var(--rock-light)"/>
        <stop offset="0.55" stop-color="var(--sand)"/>
        <stop offset="1" stop-color="var(--rust)"/>
      </linearGradient>
    </defs>

    <circle class="sun" cx="484" cy="345" r="213" fill="url(#sunFill)"
            role="img" aria-label="Textured orange setting sun"/>

    <path class="landscape"
          d="M0,445 C150,452 330,520 560,470 C760,420 920,250 1200,205
             L1200,655 C1060,700 950,752 760,775 C500,800 250,770 0,725 Z"
          fill="url(#landFill)"
          role="img"
          aria-label="Desert valley with grey mesas, sand dunes and a lone rider crossing the plain"/>

    <text class="numeral" x="302" y="810" font-size="650"
          textLength="666" lengthAdjust="spacingAndGlyphs">IV</text>
  </svg>

  <p class="artist">EVAN HOLLIS</p>
  <h1 class="title">
    <span class="title-line">LANTERNS<span class="title-connector">AFTER</span></span>
    <span class="title-line">RAIN</span>
  </h1>
</main>
</body>
</html>
```